Willowmere Loft B&B Business Card

This beautiful high-class B&B is looking for a business card that stands out from the rest. They are in the middle of the countryside, have chickens, geese and a dog. They also love bumble bees.

I was maybe thinking a rustic drawing / print of a bumble bee and a sketch of the house, I am not sure.. I quite like the feel of this... http://www.tarnwick-mill.co.uk/

Industry/Entity Type

Business

Contact Information for Business Card

Willowmere Loft
Bed & Breakfast
Brackleford, Hensworth, Somerset, TA14 7QP
01632 960418 | www.willowmereloft.co.uk

```html
<!DOCTYPE html>
<html lang="en">
<head>
<meta charset="utf-8">
<title>Willowmere Loft B&amp;B Business Card</title>
<link rel="stylesheet" href="https://fonts.googleapis.com/css2?family=Lato:wght@400;700&display=swap">
<style>
  :root {
    --stage: #e9e7e2;
    --card: #ffffff;
    --green: #1f8a1f;
    --ink: #2b2b2b;
    --sketch-dark: #9c9c9c;
    --sketch-mid: #cdcdcd;
    --sketch-light: #eeeeee;
  }
  * { margin: 0; padding: 0; box-sizing: border-box; }
  html, body { width: 1200px; height: 822px; overflow: hidden; }
  body {
    background: var(--stage);
    font-family: 'Lato', sans-serif;
    position: relative;
  }
  .card {
    position: absolute;
    width: 560px;
    height: 320px;
    background: var(--card);
    box-shadow: 0 6px 18px rgba(0,0,0,0.18);
    overflow: hidden;
  }
  .card--front { left: 320px; top: 70px; }
  .card--back { left: 320px; top: 432px; }

  /* Front */
  .front-sketch {
    position: absolute;
    inset: 0;
    background:
      radial-gradient(ellipse 70% 60% at 55% 35%, rgba(150,150,150,0.55), rgba(255,255,255,0) 70%),
      linear-gradient(165deg, var(--sketch-dark) 0%, var(--sketch-mid) 30%, var(--sketch-light) 60%, #ffffff 88%);
  }
  .brand {
    position: absolute;
    display: flex;
    flex-direction: column;
    align-items: flex-start;
  }
  .brand__tagline {
    font-weight: 400;
    text-transform: uppercase;
    color: var(--ink);
    letter-spacing: 0.3px;
    line-height: 1;
  }
  .brand__name {
    font-weight: 700;
    color: var(--green);
    line-height: 1.05;
    white-space: nowrap;
  }
  .card--front .brand { left: 120px; bottom: 40px; }
  .card--front .brand__tagline { font-size: 20px; margin-left: 4px; margin-bottom: 4px; }
  .card--front .brand__name { font-size: 50px; }

  /* Back */
  .card--back .brand { left: 48px; top: 126px; }
  .card--back .brand__tagline { font-size: 12px; margin-left: 2px; margin-bottom: 3px; }
  .card--back .brand__name { font-size: 30px; }

  .back-divider {
    position: absolute;
    left: 318px;
    top: 98px;
    width: 1.5px;
    height: 100px;
    background: var(--green);
  }
  .contact {
    position: absolute;
    left: 340px;
    top: 100px;
    font-size: 13px;
    line-height: 1.55;
    color: var(--ink);
    list-style: none;
  }
  .contact li { display: flex; align-items: center; gap: 7px; white-space: nowrap; }
  .contact svg { width: 11px; height: 11px; flex: none; }
  .back-band {
    position: absolute;
    left: 0;
    right: 0;
    bottom: 0;
    height: 10px;
    background: var(--green);
  }
</style>
</head>
<body>
  <section class="card card--front">
    <div class="front-sketch" role="img" aria-label="Pencil sketch of a stone barn house with a tree and chickens in the front yard"></div>
    <div class="brand">
      <span class="brand__tagline">Bed &amp; Breakfast</span>
      <span class="brand__name">Willowmere Loft</span>
    </div>
  </section>

  <section class="card card--back">
    <div class="brand">
      <span class="brand__tagline">Bed &amp; Breakfast</span>
      <span class="brand__name">Willowmere Loft</span>
    </div>
    <div class="back-divider"></div>
    <ul class="contact">
      <li>Brackleford, Hensworth</li>
      <li>Somerset, TA14 7QP</li>
      <li>
        <svg viewBox="0 0 24 24" aria-hidden="true"><path fill="#1f8a1f" d="M6.6 10.8a15.1 15.1 0 0 0 6.6 6.6l2.2-2.2c.3-.3.7-.4 1-.2 1.1.4 2.3.6 3.6.6.6 0 1 .4 1 1V20c0 .6-.4 1-1 1A17 17 0 0 1 3 4c0-.6.4-1 1-1h3.5c.6 0 1 .4 1 1 0 1.3.2 2.5.6 3.6.1.3 0 .7-.2 1z"/></svg>
        01632 960418
      </li>
      <li>
        <svg viewBox="0 0 24 24" aria-hidden="true"><circle cx="12" cy="12" r="10" fill="#1f8a1f"/><path d="M2 12h20M12 2c3 3 3 17 0 20M12 2c-3 3-3 17 0 20" stroke="#fff" stroke-width="1.4" fill="none"/></svg>
        www.willowmereloft.co.uk
      </li>
    </ul>
    <div class="back-band"></div>
  </section>
</body>
</html>
```